Unique Concept Design to Website Needed

Please see the attached folder. I have random images,etc but most importantly I have an attached image I was working on as a concept of a website. The brown background with blue and brown squares. logo in upper left and a little about me and then the squares would have names on them to lead to a section of the website with more info. I envision, when you mouse over a square, an image would appear so I attached random images here as well. Maybe some squares already have some images too.
- I want simple fonts. i like CLEAN, fonts
- text should be minimal. i am changing my site to less text, more powerful, bolder, larger lines with less content
- i am not sold on brown as the secondary color. i like blue but maybe grays, whites, offwhite scales or some other colors
-i have another graphic in there too
-you can see from my mock what company i am. please feel free to look me up and pull any portfolio , info , etc content to help make a great mock.
Do something cool!

```html
<!DOCTYPE html>
<html lang="en">
<head>
<meta charset="utf-8">
<title>brisk web solutions, llc</title>
<link rel="stylesheet" href="https://fonts.googleapis.com/css2?family=Source+Sans+3:wght@300;400&display=swap">
<style>
  :root {
    --bg: #cfd8c6;
    --blue: #56b0e5;
    --grey: #9b9b9b;
    --sage: #b7c1ae;
    --brand: #55aee3;
    --ink: #6a5a45;
    --label: #5b5448;
    --white: #ffffff;
  }
  html, body {
    margin: 0;
    width: 1200px;
    height: 1015px;
    overflow: hidden;
    background: var(--bg);
    font-family: "Source Sans 3", "Myriad Pro", sans-serif;
  }
  .stage {
    position: absolute;
    left: 0; top: 0;
    width: 980px;
    height: 829px;
    transform: scale(1.2245);
    transform-origin: 0 0;
  }
  .brand {
    position: absolute;
    left: 8px; top: 28px;
    margin: 0;
    color: var(--brand);
    font-weight: 300;
    line-height: 1;
  }
  .brand-name { display: block; font-size: 50px; letter-spacing: -0.5px; }
  .brand-line { display: block; font-size: 22px; margin: 2px 0 0 22px; }
  .intro {
    position: absolute;
    left: 80px; top: 176px;
    width: 320px;
    margin: 0;
    color: var(--ink);
    font-size: 13.4px;
    line-height: 18px;
    font-weight: 400;
  }
  .tile {
    position: absolute;
    width: 38px; height: 38px;
  }
  .tile.big { width: 76px; height: 76px; }
  .blue { background: var(--blue); }
  .grey { background: var(--grey); }
  .sage { background: var(--sage); }
  .tl { border-top-left-radius: 14px; }
  .tr { border-top-right-radius: 14px; }
  .bl { border-bottom-left-radius: 14px; }
  .br { border-bottom-right-radius: 14px; }
  .big.tl { border-top-left-radius: 28px; }
  .big.tr { border-top-right-radius: 28px; }
  .big.bl { border-bottom-left-radius: 28px; }
  .big.br { border-bottom-right-radius: 28px; }
  .photo {
    position: absolute;
  }
  .photo.office { background: linear-gradient(90deg, #c9b48f, #6f5a3e 45%, #a28a66 70%, #4a3a2a); }
  .photo.portrait { background: linear-gradient(180deg, #7a6a3e, #b59c6a 50%, #5e5338); }
  .photo.studio { background: linear-gradient(100deg, #d8d8d8, #7a7a7a 40%, #b9b9b9 70%, #3d3d3d); border-bottom-right-radius: 28px; }
  .photo.lamp { background: radial-gradient(ellipse at 40% 55%, #e8eef2 0%, #8d9398 30%, #2a2c2e 70%); }
  .nav {
    position: absolute;
    font-size: 11.5px;
    line-height: 1;
    white-space: nowrap;
  }
  .nav.light { color: var(--white); }
  .nav.dark { color: var(--label); }
</style>
</head>
<body>
<div class="stage">
  <h1 class="brand">
    <span class="brand-name">brisk</span>
    <span class="brand-line">web solutions, llc</span>
  </h1>
  <p class="intro">Daniel Marsh is a digital marketing consulting developing websites, promoting websites, and creating digitial video &amp; media, for businesses.</p>

  <!-- top cluster -->
  <div class="tile sage" style="left:505px;top:44px"></div>
  <div class="tile sage tr" style="left:544px;top:44px"></div>
  <div class="tile blue tl" style="left:505px;top:83px"></div>
  <div class="tile sage" style="left:544px;top:83px"></div>
  <div class="tile sage" style="left:505px;top:122px"></div>
  <div class="tile sage br" style="left:544px;top:122px"></div>
  <div class="tile blue tl" style="left:583px;top:44px"></div>
  <div class="tile blue" style="left:622px;top:44px"></div>
  <div class="tile blue" style="left:583px;top:83px"></div>
  <div class="tile blue" style="left:622px;top:83px"></div>
  <div class="tile blue bl" style="left:583px;top:122px"></div>
  <div class="tile blue" style="left:622px;top:122px"></div>
  <div class="tile grey tl" style="left:661px;top:44px"></div>
  <div class="tile grey tr" style="left:700px;top:44px"></div>
  <div class="tile grey" style="left:661px;top:83px"></div>
  <div class="tile grey" style="left:700px;top:83px"></div>
  <div class="tile grey bl" style="left:661px;top:122px"></div>
  <div class="tile grey br" style="left:700px;top:122px"></div>
  <span class="nav light" style="left:703px;top:97px">Promo</span>

  <!-- connecting column -->
  <div class="tile sage tl" style="left:427px;top:83px"></div>
  <div class="tile sage tr" style="left:466px;top:83px"></div>
  <div class="tile blue tl" style="left:427px;top:122px"></div>
  <div class="tile sage" style="left:466px;top:122px"></div>
  <div class="tile sage" style="left:427px;top:161px"></div>
  <div class="tile sage br" style="left:466px;top:161px"></div>
  <div class="tile blue" style="left:427px;top:200px"></div>
  <div class="tile blue tr" style="left:466px;top:200px"></div>

  <!-- middle cluster -->
  <div class="tile sage tl" style="left:349px;top:239px"></div>
  <div class="tile sage" style="left:388px;top:239px"></div>
  <div class="tile blue" style="left:427px;top:239px"></div>
  <div class="tile blue" style="left:466px;top:239px"></div>
  <div class="tile grey tl" style="left:505px;top:239px"></div>
  <div class="tile grey tr" style="left:544px;top:239px"></div>
  <div class="tile blue tl" style="left:349px;top:278px"></div>
  <div class="photo office" role="img" aria-label="Photo of a home office desk" style="left:388px;top:278px;width:77px;height:38px"></div>
  <div class="tile blue br" style="left:466px;top:278px"></div>
  <div class="tile grey" style="left:505px;top:278px"></div>
  <div class="tile grey" style="left:544px;top:278px"></div>
  <div class="tile sage" style="left:349px;top:317px"></div>
  <div class="tile sage" style="left:388px;top:317px"></div>
  <div class="tile blue" style="left:427px;top:317px"></div>
  <div class="tile blue" style="left:466px;top:317px"></div>
  <div class="tile grey bl" style="left:505px;top:317px"></div>
  <div class="tile grey" style="left:544px;top:317px"></div>
  <div class="tile blue bl" style="left:349px;top:356px"></div>
  <div class="tile blue" style="left:388px;top:356px"></div>
  <div class="tile grey" style="left:427px;top:356px"></div>
  <div class="tile grey" style="left:466px;top:356px"></div>
  <div class="tile sage" style="left:505px;top:356px"></div>
  <div class="tile blue tr" style="left:544px;top:356px"></div>
  <span class="nav dark" style="left:391px;top:329px">Media</span>
  <span class="nav dark" style="left:468px;top:332px">design</span>

  <!-- lower left cluster -->
  <div class="tile sage tl" style="left:232px;top:395px"></div>
  <div class="photo portrait" role="img" aria-label="Portrait photo of the consultant" style="left:271px;top:395px;width:38px;height:77px"></div>
  <div class="tile blue tl" style="left:310px;top:395px"></div>
  <div class="tile blue tr" style="left:349px;top:395px"></div>
  <div class="tile grey tl" style="left:388px;top:395px"></div>
  <div class="tile grey tr" style="left:427px;top:395px"></div>
  <div class="tile blue tl" style="left:232px;top:434px"></div>
  <div class="tile blue" style="left:310px;top:434px"></div>
  <div class="tile blue" style="left:349px;top:434px"></div>
  <div class="tile grey" style="left:388px;top:434px"></div>
  <div class="tile grey" style="left:427px;top:434px"></div>
  <div class="tile sage" style="left:232px;top:473px"></div>
  <div class="tile sage br" style="left:271px;top:473px"></div>
  <div class="tile blue bl" style="left:310px;top:473px"></div>
  <div class="tile blue" style="left:349px;top:473px"></div>
  <div class="tile grey" style="left:388px;top:473px"></div>
  <div class="tile grey br" style="left:427px;top:473px"></div>
  <div class="tile blue bl" style="left:232px;top:512px"></div>
  <div class="tile blue" style="left:271px;top:512px"></div>
  <div class="tile grey" style="left:310px;top:512px"></div>
  <div class="tile grey" style="left:349px;top:512px"></div>
  <div class="tile sage" style="left:388px;top:512px"></div>
  <div class="tile blue tr" style="left:427px;top:512px"></div>

  <!-- right large cluster -->
  <div class="tile big blue tl" style="left:661px;top:161px"></div>
  <div class="tile big blue tr" style="left:739px;top:161px"></div>
  <div class="photo studio" role="img" aria-label="Black and white photo of a workspace" style="left:661px;top:239px;width:155px;height:76px;border-top-left-radius:28px"></div>
  <div class="tile big blue tl" style="left:817px;top:239px"></div>
  <div class="tile big blue tr" style="left:895px;top:239px"></div>
  <div class="tile big blue" style="left:661px;top:317px"></div>
  <div class="tile big blue" style="left:739px;top:317px"></div>
  <div class="tile big blue" style="left:817px;top:317px"></div>
  <div class="tile big blue" style="left:895px;top:317px"></div>
  <div class="tile big blue bl" style="left:661px;top:395px"></div>
  <div class="tile big blue br" style="left:739px;top:395px"></div>
  <span class="nav dark" style="left:745px;top:422px">Testimonials</span>
  <div class="tile big blue tl" style="left:661px;top:473px"></div>
  <div class="tile big blue tr" style="left:739px;top:473px"></div>
  <span class="nav dark" style="left:678px;top:500px">Pay Online</span>
  <div class="tile big blue tl" style="left:661px;top:551px"></div>
  <div class="photo lamp" role="img" aria-label="Photo of a studio light" style="left:739px;top:551px;width:77px;height:149px"></div>
  <div class="tile big blue tr" style="left:817px;top:551px"></div>
  <div class="tile big blue" style="left:661px;top:629px"></div>
  <div class="tile big blue br" style="left:817px;top:629px"></div>
  <div class="tile big blue bl" style="left:661px;top:707px"></div>
  <div class="tile big blue br" style="left:739px;top:707px"></div>
</div>
</body>
</html>
```